PEACFUL ACUPUNCTURE PRACTITIONER NEEDS A NEW COAT

I need a new design for an exiting website http://stillwillowneedlework.example/ for a acupuncturist. This will be a minimalism design with lots and lots of white space. Home page and one interior page. Please keep the feeling of calm and peaceful serenity. For Color scheme: https://www.harborfernclinic.example/fertility. The bottom part of the home page with sections and links to the service pages: https://mossgatewellness.example/. The client likes this the best: http://qlhealing.example/. I'm attaching the logo and content pages.

Target Market(s)

Women

Industry/Entity Type

Wellness, health, wellbeing, meditation

Number of Pages Required

2 page

Font styles to use
Sans Serif
Decorative

Colors

Designer to choose colors to be used in the design.

Requirements
Must have
Nice to have
• Follow new website drafts and links
Should not have
• Busy with bright colors. No poping

```html
<!DOCTYPE html>
<html lang="en">
<head>
<meta charset="utf-8">
<title>Still Willow Acupuncture</title>
<link href="https://fonts.googleapis.com/css2?family=Roboto+Slab:wght@300;400&family=Roboto:wght@300;400&display=swap" rel="stylesheet">
<style>
:root{
  --mauve:#b07a80;
  --mauve-dark:#9c6a70;
  --blush:#dbc3c8;
  --ink:#333;
  --muted:#555;
  --footer:#1e1e1e;
  --faq-bg:#f1f0f0;
  --white:#fff;
}
*{margin:0;padding:0;box-sizing:border-box}
html,body{width:1200px;height:3683px;overflow:hidden;background:var(--white)}
body{font-family:'Roboto Slab',serif;color:var(--ink);position:relative}
.abs{position:absolute}
.header{top:0;left:0;width:1200px;height:129px}
.brand{left:112px;top:36px;display:flex;align-items:center;gap:12px}
.brand-dot{width:54px;height:54px;border-radius:50%;background:var(--blush)}
.brand-name{font-family:'Roboto Slab',serif;font-weight:400;color:var(--mauve-dark);line-height:1}
.brand-name .big{font-size:36px;display:block}
.brand-name .small{font-size:19px;letter-spacing:4px;display:block;margin-top:2px}
.call{left:876px;top:30px;display:flex;align-items:center;gap:14px}
.call-circle{width:64px;height:64px;border-radius:50%;background:var(--mauve);display:flex;align-items:center;justify-content:center}
.call-text{font-family:'Roboto',sans-serif;color:#555;font-size:15px;line-height:1.4}
.call-text b{display:block;font-weight:400;font-size:23px;color:#444}
.nav{top:129px;left:0;width:1200px;height:64px;background:var(--mauve);display:flex;justify-content:center;align-items:center;gap:27px}
.nav a{color:#fff;text-decoration:none;font-size:14px}
.hero{top:193px;left:0;width:1200px;height:682px;background:radial-gradient(ellipse at 55% 30%,#d79f7a 0%,#b87a55 40%,#7a4a32 100%)}
.hero-text{left:772px;top:376px;color:#fff}
.hero-text h1{font-weight:400;font-size:56px;line-height:1.05}
.hero-text h2{font-weight:400;font-size:38px;line-height:1.2;margin-top:6px}
.hero-text p{font-weight:300;font-size:18px;line-height:30px;margin-top:22px;width:360px;padding-left:4px}
.btn{display:inline-block;margin:28px 0 0 6px;border:2px solid #fff;color:#fff;font-size:17px;padding:12px 24px}
.section-title{width:1200px;left:0;text-align:center;font-weight:300;font-size:40px;color:#333}
.rule{height:3px;width:56px;background:var(--mauve)}
.focus-box{top:1030px;width:236px;height:210px;border:5px solid var(--mauve);text-align:center;color:var(--mauve);font-size:20px;line-height:31px;padding-top:18px}
.focus-box svg{display:block;margin:0 auto 12px}
.philo{top:1326px;left:0;width:619px;height:508px;background:var(--blush)}
.philo h3{position:absolute;left:110px;top:82px;font-weight:300;font-size:40px;color:#333}
.philo .rule{position:absolute;left:110px;top:140px}
.philo p{position:absolute;left:112px;width:472px;font-family:'Roboto Slab',serif;font-size:14px;line-height:27.5px;color:#333;text-align:justify}
.philo-img{top:1326px;left:619px;width:581px;height:508px;background:linear-gradient(135deg,#e9d6cc 0%,#d9b8a6 40%,#c9a08a 70%,#efe2da 100%)}
.feature{width:480px}
.feature .ring{position:absolute;left:0;top:0;width:112px;height:112px;border-radius:50%;border:2px solid var(--mauve);display:flex;align-items:center;justify-content:center}
.feature h4{position:absolute;left:144px;top:4px;font-weight:400;font-size:23px;color:var(--mauve);white-space:nowrap}
.feature p{position:absolute;left:144px;top:44px;width:326px;font-family:'Roboto',sans-serif;font-size:13.5px;line-height:26px;color:#444}
.testi{top:2346px;left:0;width:1200px;height:479px;background:linear-gradient(90deg,#c99298 0%,#bf868c 50%,#c48d93 100%)}
.testi h3{position:absolute;width:1200px;text-align:center;top:80px;font-weight:300;font-size:42px;color:#fff}
.testi .rule{position:absolute;left:572px;top:143px;background:#fff}
.testi p{position:absolute;left:250px;width:700px;top:168px;text-align:center;color:#fff;font-size:14.5px;line-height:30px;font-weight:300}
.testi .name{position:absolute;width:1200px;text-align:center;top:336px;color:#fff;font-size:21px}
.testi .stars{position:absolute;width:1200px;text-align:center;top:372px;color:#fff;font-size:15px;letter-spacing:3px}
.faq{top:2825px;left:0;width:1200px;height:551px;background:linear-gradient(90deg,#ece6e3 0%,var(--faq-bg) 45%,#f4f4f4 100%)}
.faq-item{left:280px;width:640px;height:52px;background:#fff;border:1px solid #ddd;display:flex;align-items:center;padding-left:14px;font-size:15.5px;color:#333}
.faq-item span{font-size:26px;color:#444;margin-right:12px}
.footer{top:3376px;left:0;width:1200px;height:307px;background:var(--footer);color:#fff}
.footer .fbrand{position:absolute;left:156px;top:32px;width:248px;text-align:center;color:#eee}
.footer .fdot{width:100px;height:100px;border-radius:50%;background:var(--mauve);margin:0 auto 16px}
.footer .fbrand .big{font-size:36px;display:block;line-height:1}
.footer .fbrand .small{font-size:21px;letter-spacing:5px;display:block}
.vline{width:1px;background:#444;top:48px;height:122px}
.finfo{font-size:15.5px;line-height:24px;color:#fff}
.social{width:42px;height:42px;border-radius:50%;border:2px solid #fff}
.fsep{left:112px;top:230px;width:976px;height:1px;background:#3a3a3a}
.copy{top:262px;width:1200px;left:0;text-align:center;font-size:15.5px}
</style>
</head>
<body>
<header class="abs header">
  <div class="abs brand"><div class="brand-dot"></div><div class="brand-name"><span class="big">Still Willow</span><span class="small">ACUPUNCTURE</span></div></div>
  <div class="abs call">
    <div class="call-circle"><svg width="22" height="22" viewBox="0 0 24 24"><path d="M6.6 10.8a15 15 0 0 0 6.6 6.6l2.2-2.2a1 1 0 0 1 1-.25 11.4 11.4 0 0 0 3.6.6 1 1 0 0 1 1 1V20a1 1 0 0 1-1 1A17 17 0 0 1 3 4a1 1 0 0 1 1-1h3.5a1 1 0 0 1 1 1c0 1.25.2 2.45.6 3.6a1 1 0 0 1-.25 1z" fill="#fff"/></svg></div>
    <div class="call-text">Call Us :<b>555-014-2290</b></div>
  </div>
</header>
<nav class="abs nav">
  <a>Home</a><a>About</a><a>Fertility &amp; Pregnancy</a><a>Hormone Balance</a><a>Strength &amp; Structure</a><a>Emotional wellbeing</a><a>Online Shop</a><a>Testimonials</a>
</nav>

<section class="abs hero" role="img" aria-label="Photo of a practitioner placing acupuncture needles in a client's shoulder"></section>
<div class="abs hero-text">
  <h1>Still Willow</h1>
  <h2>Acupuncture</h2>
  <p>Specializing In women's health,fertility challenges &amp; Pregnancy care</p>
  <span class="btn">Read More</span>
</div>

<h2 class="abs section-title" style="top:918px">Areas of Focus</h2>
<div class="abs rule" style="left:572px;top:980px"></div>
<div class="abs focus-box" style="left:112px">
  <svg width="64" height="80" viewBox="0 0 64 80" fill="none" stroke="#b07a80" stroke-width="2.5"><path d="M26 4c-8 10 8 16 0 28s6 22-4 30"/><path d="M42 8c8 12-6 18 2 28s-4 22 4 32"/><circle cx="30" cy="44" r="8"/></svg>
  Fertility &amp;<br>Pregnancy
</div>
<div class="abs focus-box" style="left:359px">
  <svg width="80" height="80" viewBox="0 0 80 80" fill="none" stroke="#b07a80" stroke-width="2.5"><circle cx="40" cy="40" r="36"/><path d="M26 52h28"/></svg>
  Emotional Well<br>Being
</div>
<div class="abs focus-box" style="left:606px">
  <svg width="86" height="80" viewBox="0 0 86 80" fill="none" stroke="#b07a80" stroke-width="2.5"><path d="M22 44l10-6 10 6v12l-10 6-10-6z"/><path d="M42 32l10-6 10 6v12l-10 6-10-6z"/><path d="M62 32l8-10M22 56l-10 6M52 26V12"/><circle cx="74" cy="18" r="3"/><circle cx="10" cy="64" r="3"/></svg>
  Hormone<br>Balance
</div>
<div class="abs focus-box" style="left:853px">
  <svg width="80" height="80" viewBox="0 0 80 80" fill="none" stroke="#b07a80" stroke-width="2.5"><circle cx="40" cy="12" r="7"/><path d="M40 19v14M40 33L16 62M40 33l24 29M40 33v29M28 47h24"/><circle cx="16" cy="66" r="5"/><circle cx="34" cy="66" r="5"/><circle cx="48" cy="66" r="5"/><circle cx="64" cy="66" r="5"/></svg>
  Strength &amp;<br>Structure
</div>

<section class="abs philo">
  <h3>Philosophy of Care</h3>
  <div class="rule"></div>
  <p style="top:178px">Acupuncture &amp; Chinese Herbal Medicine are rooted in over 3000 years of history and tradition. As a complete medical system that has remained flexible and relevant we honor what has worked from the past while embracing the medicine of tomorrow.</p>
  <p style="top:315px">At Still Willow Acupuncture we provide compassionate, respectful and empowering care in a safe and inclusive environment. Our goal is to harmonize physical, mental and emotional wellbeing strengthen the still point from which we all strive to live.</p>
</section>
<div class="abs philo-img" role="img" aria-label="Photo of a relaxed woman receiving facial acupuncture"></div>

<div class="abs feature" style="left:112px;top:1924px">
  <div class="ring"><svg width="54" height="62" viewBox="0 0 54 62" fill="none" stroke="#b07a80" stroke-width="2.5"><path d="M27 3L5 11v18c0 15 10 25 22 30 12-5 22-15 22-30V11z"/><rect x="18" y="28" width="18" height="15" rx="2"/><path d="M21 28v-5a6 6 0 0 1 12 0v5"/></svg></div>
  <h4>Non-Discrimination Policy</h4>
  <p>Still Willow Acupuncture does not discriminate on basis of race or national origin, age, religion, ability, education, height, weight, body type, marital status, sexual orientation, sex, or gender identity.</p>
</div>
<div class="abs feature" style="left:626px;top:1924px">
  <div class="ring"><svg width="62" height="62" viewBox="0 0 62 62" fill="none" stroke="#b07a80" stroke-width="2.5"><circle cx="31" cy="31" r="28"/><circle cx="31" cy="16" r="4" fill="#b07a80"/><path d="M17 24l14 4 14-4M31 28v10l-7 12M31 38l7 12"/></svg></div>
  <h4>Accessibility</h4>
  <p>6 carpeted stairs with railing. Unfortunately, no elevator or ramp. Gender inclusive restroom. Not a scent free environment.</p>
</div>
<div class="abs feature" style="left:112px;top:2140px">
  <div class="ring"><svg width="44" height="64" viewBox="0 0 44 64" fill="none" stroke="#b07a80" stroke-width="2.5"><rect x="10" y="4" width="6" height="22" rx="3"/><rect x="28" y="4" width="6" height="22" rx="3"/><path d="M13 26v32M31 26v32M4 58h14M26 58h14"/></svg></div>
  <h4>About Acupuncture</h4>
  <p>Acupuncture is the insertion of thin needles at specific points which act as guideposts for healing. These guideposts help the body use its own mechanisms for selfregulation to restore health.</p>
</div>
<div class="abs feature" style="left:626px;top:2140px">
  <div class="ring"><svg width="62" height="54" viewBox="0 0 62 54" fill="none" stroke="#b07a80" stroke-width="2.5"><path d="M6 24h50c0 14-11 22-25 22S6 38 6 24z"/><path d="M22 46v4h18v-4"/><path d="M44 22L56 6M22 22c-6-4-10-10-8-16 6 2 10 8 8 16zM32 22c2-6 8-10 14-8-2 6-8 10-14 8z"/></svg></div>
  <h4>About Herbs</h4>
  <p>Herbal formulas aid in extending and enhancing acupuncture treatments. Daily use acts as a reinforcing agent, encouraging the body towards a healthier path until it is strong enough to take over on its own.</p>
</div>

<section class="abs testi" role="img" aria-label="Soft mauve backdrop with faded treatment photo">
  <h3>Our Testimonials</h3>
  <div class="rule"></div>
  <svg class="abs" style="left:128px;top:182px" width="24" height="116" viewBox="0 0 24 116" fill="none" stroke="#fff" stroke-width="2"><path d="M22 2L2 58l20 56"/></svg>
  <svg class="abs" style="left:1046px;top:182px" width="24" height="116" viewBox="0 0 24 116" fill="none" stroke="#fff" stroke-width="2"><path d="M2 2l20 56-20 56"/></svg>
  <p>&#10077; Mara is such an incredibly skilled, competent and knowledgeable practitioner. I started seeing Mara because after a year and a half of trying to conceive, and suffering a miscarriage along the way, I was about to embark on trying IVF and I wanted extra support. I had used acupuncture before, but several friends suggested that I see Mara specifically because of her extensive experience with working with clients who are undergoing IVF and have had challenges conceiving. &#10078;</p>
  <div class="name">Dummy Name</div>
  <div class="stars">★★★★★</div>
</section>

<section class="abs faq" role="img" aria-label="Faded photo of facial acupuncture treatment behind the questions"></section>
<h2 class="abs section-title" style="top:2875px">Our Faq's</h2>
<div class="abs rule" style="left:572px;top:2937px"></div>
<div class="abs faq-item" style="top:2975px"><span>Q.</span>How Do I Know If Acupuncture Can Help Me?</div>
<div class="abs faq-item" style="top:3039px"><span>Q.</span>Does Acupuncture Hurt?</div>
<div class="abs faq-item" style="top:3104px"><span>Q.</span>How Big Are The Needles And Are They Sterile?</div>
<div class="abs faq-item" style="top:3167px"><span>Q.</span>What Are Treatments Like And How Long Do They Take?</div>
<div class="abs faq-item" style="top:3231px"><span>Q.</span>How Many Treatments Will I Need?</div>

<footer class="abs footer">
  <div class="fbrand"><div class="fdot"></div><span class="big">Still Willow</span><span class="small">ACUPUNCTURE</span></div>
  <div class="abs vline" style="left:445px"></div>
  <div class="abs vline" style="left:774px"></div>
  <svg class="abs" style="left:472px;top:68px" width="18" height="24" viewBox="0 0 18 24" fill="none" stroke="#fff" stroke-width="1.6"><path d="M9 23S1 13 1 8a8 8 0 0 1 16 0c0 5-8 15-8 15z"/><circle cx="9" cy="8" r="3"/></svg>
  <div class="abs finfo" style="left:511px;top:60px">Address<br>14 Alder Row<br>Fairhaven, MA 01099</div>
  <div class="abs social" style="left:511px;top:135px"></div>
  <div class="abs social" style="left:563px;top:135px"></div>
  <svg class="abs" style="left:814px;top:68px" width="20" height="20" viewBox="0 0 24 24" fill="none" stroke="#fff" stroke-width="1.5"><path d="M6.6 10.8a15 15 0 0 0 6.6 6.6l2.2-2.2a1 1 0 0 1 1-.25 11.4 11.4 0 0 0 3.6.6 1 1 0 0 1 1 1V20a1 1 0 0 1-1 1A17 17 0 0 1 3 4a1 1 0 0 1 1-1h3.5a1 1 0 0 1 1 1c0 1.25.2 2.45.6 3.6a1 1 0 0 1-.25 1z"/></svg>
  <div class="abs finfo" style="left:852px;top:58px">Phone:<br>555-014-2290</div>
  <svg class="abs" style="left:814px;top:136px" width="22" height="16" viewBox="0 0 22 16" fill="none" stroke="#fff" stroke-width="1.5"><rect x="1" y="1" width="20" height="14"/><path d="M1 1l10 8 10-8"/></svg>
  <div class="abs finfo" style="left:855px;top:127px">Email:<br>mara@stillwillowneedlework.example</div>
  <div class="abs fsep"></div>
  <div class="abs copy">Still Willow Acupuncture &nbsp;© 2021.All Rights Reserved.</div>
</footer>
</body>
</html>
```